"Cork Hollow Excursions" is a top notch Santa Barbara County Wine Tour company.

We provide scenic, boutique and custom wine tours. I need the card to be clean and classy. I will provide our logo. I would like the logo to cover the back side of the card as an option and would like to see a couple color options other then our signature green and gold. I would like to see some creative options and let the designers come up with options.
I need cards for myself and my team. The final design should communicate "An authentic and boutique wine tour experience"
Please use my website for reference www.corkhollowexcursions.com

Target Market(s)

We have a wide range of clients from millennials to baby boomers

Industry/Entity Type

Tour

Contact Information for Business Card

Contact info:
Dale Munford
805-291-6384
info@corkhollowexcursions.com
corkhollowexcursions.com

Colors

Designer to choose colors to be used in the design.

Requirements
Must have
• my logo
Nice to have
• *I would like to have the backside side with the logo and the company statement
• "An authentic and boutique wine tour experience" as an option.
• *I would also like to see what the designers can create!
• *I would like to see an option that incorporates or social: snapgrid, rovia, route scout
Should not have
• I do not want it too busy.

```html
<!DOCTYPE html>
<html lang="en">
<head>
<meta charset="UTF-8">
<title>Cork Hollow Excursions — Business Cards</title>
<link rel="stylesheet" href="https://fonts.googleapis.com/css2?family=Roboto:wght@400;500;700&display=swap">
<style>
  :root {
    --backdrop: #e4e5e8;
    --card: #ffffff;
    --gold: #c9ab6b;
    --gold-light: #e3d2ab;
    --gold-pale: #f3ead7;
    --gold-deep: #a8874a;
    --taupe: #8c7a62;
    --ink: #3c3c3c;
    --green: #2f6b35;
  }
  * { box-sizing: border-box; margin: 0; padding: 0; }
  html, body {
    width: 1200px; height: 800px; overflow: hidden;
    background: var(--backdrop);
    font-family: "Roboto", Arial, sans-serif;
  }
  .sheet {
    width: 1200px; height: 800px;
    display: flex; align-items: center; justify-content: center; gap: 36px;
  }
  .card {
    position: relative;
    width: 546px; height: 312px;
    background: var(--card);
    overflow: hidden;
    box-shadow: 0 8px 20px rgba(0,0,0,0.14);
  }
  .card__scene {
    position: absolute; left: 0; bottom: 24px;
    width: 100%; height: 190px;
    display: block;
  }
  .card__band {
    position: absolute; left: 0; right: 0; bottom: 0;
    height: 24px;
    background: linear-gradient(90deg, var(--gold-deep), var(--gold) 45%, #dcc38e 70%, var(--gold));
  }
  .brand {
    position: absolute;
    display: flex; flex-direction: column; align-items: center; gap: 10px;
    text-align: center; z-index: 1;
  }
  .brand__mark {
    width: 56px; height: 56px; border-radius: 50%;
    background: var(--green);
  }
  .brand__name {
    font-weight: 500;
    color: var(--taupe);
    text-transform: uppercase;
    letter-spacing: 0.06em;
    line-height: 1.1;
  }

  /* Front */
  .card--front .brand { left: 36px; top: 30px; width: 250px; }
  .card--front .brand__name { font-size: 25px; }
  .contact {
    position: absolute; left: 318px; top: 112px;
    list-style: none; z-index: 1;
  }
  .contact__name {
    font-weight: 700; font-size: 15px; color: var(--gold-deep);
    text-transform: uppercase; margin-bottom: 8px; letter-spacing: 0.02em;
  }
  .contact__item {
    display: flex; align-items: center; gap: 7px;
    font-size: 13px; color: var(--ink); margin-bottom: 6px;
  }
  .contact__icon { width: 11px; height: 11px; flex: none; }

  /* Back */
  .card--back .brand { left: 0; right: 0; top: 44px; }
  .card--back .brand__mark { width: 70px; height: 70px; }
  .card--back .brand__name { font-size: 36px; }
</style>
</head>
<body>
<main class="sheet">

  <section class="card card--front" aria-label="Business card front">
    <svg class="card__scene" viewBox="0 0 546 190" preserveAspectRatio="none" role="img" aria-label="Engraved gold vineyard landscape with rolling hills, trees, farmhouse, wine bottle and glass">
      <defs>
        <linearGradient id="sceneFront" x1="0" y1="0" x2="0" y2="1">
          <stop offset="0" stop-color="var(--gold-pale)"/>
          <stop offset="1" stop-color="var(--gold-light)"/>
        </linearGradient>
      </defs>
      <path d="M0 40 C120 20 220 70 300 90 C380 110 460 120 546 150 L546 190 L0 190 Z" fill="url(#sceneFront)"/>
    </svg>
    <div class="brand">
      <span class="brand__mark"></span>
      <span class="brand__name">Cork Hollow Excursions</span>
    </div>
    <ul class="contact">
      <li class="contact__name">Dale Munford</li>
      <li class="contact__item">
        <svg class="contact__icon" viewBox="0 0 12 12"><circle cx="6" cy="6" r="5.3" fill="none" stroke="var(--gold)" stroke-width="1"/><path d="M4 3.5l1 1-.6.8c.4.9 1 1.5 1.9 1.9l.8-.6 1 1-.7.8C5.8 8.2 3.8 6.2 3.6 4.2z" fill="var(--gold)"/></svg>
        805-291-6384
      </li>
      <li class="contact__item">
        <svg class="contact__icon" viewBox="0 0 12 12"><rect x="1" y="2.5" width="10" height="7" fill="none" stroke="var(--gold)" stroke-width="1"/><path d="M1 2.5l5 4 5-4" fill="none" stroke="var(--gold)" stroke-width="1"/></svg>
        info@corkhollowexcursions.com
      </li>
      <li class="contact__item">
        <svg class="contact__icon" viewBox="0 0 12 12"><circle cx="6" cy="6" r="5" fill="none" stroke="var(--gold)" stroke-width="1"/><ellipse cx="6" cy="6" rx="2.2" ry="5" fill="none" stroke="var(--gold)" stroke-width="0.8"/><path d="M1 6h10" stroke="var(--gold)" stroke-width="0.8"/></svg>
        corkhollowexcursions.com
      </li>
    </ul>
    <div class="card__band"></div>
  </section>

  <section class="card card--back" aria-label="Business card back">
    <svg class="card__scene" viewBox="0 0 546 190" preserveAspectRatio="none" role="img" aria-label="Engraved gold vineyard hills with trees, farmhouse and windmill">
      <defs>
        <linearGradient id="sceneBack" x1="0" y1="0" x2="0" y2="1">
          <stop offset="0" stop-color="var(--gold-pale)"/>
          <stop offset="1" stop-color="var(--gold-light)"/>
        </linearGradient>
      </defs>
      <path d="M0 20 C100 30 200 70 290 80 C380 90 470 100 546 110 L546 190 L0 190 Z" fill="url(#sceneBack)"/>
    </svg>
    <div class="brand">
      <span class="brand__mark"></span>
      <span class="brand__name">Cork Hollow Excursions</span>
    </div>
    <div class="card__band"></div>
  </section>

</main>
</body>
</html>
```